Painting Company Business Card

Brightwell Painting needs a new business card. See attachments for our logo and current card as an example.
We want to utilize the same colors in the logo, and keep all the information that is currently on it. Just need an updated and modern design.
We are open to loosing the Association Logos if it means a better design.
We are also entertaining a spot for a picture of a headshot of the person listed on the card. Head shot can be finished later.

```html
<!DOCTYPE html>
<html lang="en">
<head>
<meta charset="utf-8">
<title>Brightwell Painting – Business Card</title>
<link rel="stylesheet" href="https://fonts.googleapis.com/css2?family=Montserrat:wght@500;600;700&family=Sacramento&display=swap">
<style>
  :root {
    --card-bg: #e3e3e3;
    --card-bg-light: #ececec;
    --brand-green: #3f5b2c;
    --name-green: #3a4a2d;
    --band-red: #8b3b3a;
    --band-red-dark: #7d3231;
    --ink: #111111;
    --white: #ffffff;
    --photo-green: #3b4b2c;
  }
  html, body {
    margin: 0;
    padding: 0;
    width: 1200px;
    height: 686px;
    overflow: hidden;
    background: #ffffff;
  }
  .card {
    position: relative;
    width: 1200px;
    height: 686px;
    overflow: hidden;
    background: radial-gradient(circle at 40% 40%, var(--card-bg-light), var(--card-bg));
    font-family: "Montserrat", Arial, sans-serif;
  }
  .brand-name {
    position: absolute;
    right: 40px;
    top: 52px;
    margin: 0;
    text-align: right;
    font-family: "Montserrat", Arial, sans-serif;
    font-weight: 700;
    font-size: 60px;
    line-height: 1.05;
    color: var(--brand-green);
    letter-spacing: 1px;
    text-transform: uppercase;
  }
  .person-name {
    position: absolute;
    left: 0;
    width: 1224px;
    top: 250px;
    margin: 0;
    text-align: center;
    font-family: "Sacramento", cursive;
    font-weight: 400;
    font-size: 88px;
    line-height: 1;
    color: var(--name-green);
  }
  .person-role {
    position: absolute;
    left: 0;
    width: 1222px;
    top: 360px;
    margin: 0;
    text-align: center;
    font-weight: 500;
    font-size: 37px;
    color: var(--ink);
  }
  .contact-band {
    position: absolute;
    left: 0;
    top: 443px;
    width: 1200px;
    height: 178px;
    background: linear-gradient(180deg, var(--band-red), var(--band-red-dark));
  }
  .contact-list {
    position: absolute;
    left: 56px;
    top: 466px;
    margin: 0;
    padding: 0;
    list-style: none;
  }
  .contact-item {
    display: flex;
    align-items: center;
    height: 46px;
    font-weight: 500;
    font-size: 35px;
    color: var(--white);
    letter-spacing: 0.3px;
  }
  .contact-icon {
    width: 34px;
    height: 34px;
    margin-right: 9px;
    flex: none;
  }
  .headshot {
    position: absolute;
    left: 857px;
    top: 377px;
    width: 274px;
    height: 280px;
    border-radius: 20px;
    background: var(--photo-green);
  }
</style>
</head>
<body>
  <div class="card">
    <h1 class="brand-name">Brightwell<br>Painting</h1>

    <p class="person-name">Mark Ellison</p>
    <p class="person-role">Quality Manager</p>

    <div class="contact-band"></div>

    <ul class="contact-list">
      <li class="contact-item">
        <svg class="contact-icon" viewBox="0 0 34 34" aria-hidden="true">
          <circle cx="17" cy="17" r="16" fill="var(--ink)"/>
          <path d="M11.5 9.5c1-.9 2-.7 2.6.2l1.6 2.5c.5.8.3 1.7-.4 2.3l-1 .8c.8 1.9 2.4 3.6 4.3 4.5l.9-1c.6-.7 1.5-.8 2.3-.3l2.5 1.6c.9.6 1 1.7.2 2.6l-1.2 1.3c-1 1-2.6 1.2-4 .6-4.2-1.8-7.3-5-9-9.2-.5-1.4-.2-2.9.8-3.9z" fill="var(--white)"/>
        </svg>
        262 555 0147
      </li>
      <li class="contact-item">
        <svg class="contact-icon" viewBox="0 0 34 34" aria-hidden="true">
          <rect x="3" y="8" width="28" height="19" rx="2.5" fill="var(--ink)"/>
          <path d="M5 10.5l12 9 12-9" fill="none" stroke="var(--band-red)" stroke-width="2.4" stroke-linejoin="round"/>
        </svg>
        mark.brightwell@mailbox.com
      </li>
      <li class="contact-item">
        <svg class="contact-icon" viewBox="0 0 34 34" aria-hidden="true">
          <g fill="none" stroke="var(--ink)" stroke-width="2.4">
            <circle cx="17" cy="17" r="14"/>
            <ellipse cx="17" cy="17" rx="6" ry="14"/>
            <line x1="3" y1="17" x2="31" y2="17"/>
            <path d="M5.5 10h23M5.5 24h23"/>
          </g>
        </svg>
        brightwellpainting.com
      </li>
    </ul>

    <div class="headshot" role="img" aria-label="Headshot of the quality manager on a dark green backdrop"></div>
  </div>
</body>
</html>
```